Business Card Design

Mobile dog grooming

Industry/Entity Type

Business

Contact Information for Business Card

Bluefern Mobile Grooming
Marisol Teague
555-314-9072
www.bluefernmobilegrooming.example

```html
<!DOCTYPE html>
<html lang="en">
<head>
<meta charset="utf-8">
<title>Bluefern Mobile Grooming – Business Card</title>
<link rel="stylesheet" href="https://fonts.googleapis.com/css2?family=Quicksand:wght@300;500;700&display=swap">
<style>
  :root {
    --backdrop: #e4e4e2;
    --card: #ffffff;
    --purple: #8a62c8;
    --purple-soft: #a386d6;
    --bubble: #b9dcef;
    --tan: #d9c3a4;
    --cream: #f1ece3;
  }
  * { margin: 0; padding: 0; box-sizing: border-box; }
  html, body {
    width: 1200px;
    height: 1000px;
    overflow: hidden;
    background: var(--backdrop);
    font-family: "Quicksand", sans-serif;
  }
  .stage {
    width: 1200px;
    height: 1000px;
    display: flex;
    align-items: center;
    justify-content: center;
  }
  .card {
    width: 1050px;
    height: 600px;
    background: var(--card);
    box-shadow: 0 10px 30px rgba(0,0,0,0.12);
    display: flex;
    flex-direction: column;
    align-items: center;
    padding-top: 40px;
    color: var(--purple);
  }
  .logo {
    display: flex;
    flex-direction: column;
    align-items: center;
    gap: 10px;
  }
  .logo-art {
    width: 360px;
    height: 210px;
    border-radius: 40px;
    background: radial-gradient(circle at 40% 45%, var(--cream) 0%, var(--tan) 45%, var(--bubble) 100%);
  }
  .logo-name {
    font-weight: 700;
    font-size: 24px;
    letter-spacing: 1px;
    color: var(--purple);
  }
  .details {
    margin-top: 28px;
    text-align: center;
    line-height: 1.2;
  }
  .business-name {
    font-weight: 500;
    font-size: 44px;
  }
  .person-name {
    font-weight: 300;
    font-size: 38px;
    color: var(--purple-soft);
    margin-top: 6px;
  }
  .phone, .website {
    font-weight: 300;
    font-size: 24px;
    margin-top: 6px;
  }
</style>
</head>
<body>
  <main class="stage">
    <section class="card">
      <div class="logo">
        <div class="logo-art" role="img" aria-label="Illustration of cartoon dogs riding in a bubble-filled bathtub on wheels"></div>
        <div class="logo-name">Bluefern Mobile Grooming</div>
      </div>
      <div class="details">
        <h1 class="business-name">Bluefern Mobile Grooming</h1>
        <p class="person-name">Marisol Teague</p>
        <p class="phone">555-314-9072</p>
        <p class="website">www.bluefernmobilegrooming.example</p>
      </div>
    </section>
  </main>
</body>
</html>
```